Delegate visit agenda

We need a creative, yet simple and official design for an agenda to be handed out for delegates visiting our organization. The design needs to be creative, informative and visual when possible. Flat design is desired but other options are welcomed. The agenda should be 3 pages in lengths only. Page 1 should have the company logo with an event title (with the ability to add country flag) and the dates of the event. Pages 2 should include photos of receiving delegate (e.g. VIPs) and any other relevant people. Page 3 should include agenda entries with the following information: title of entry, date and time, location, relevant pictures (e.g. a hotel or flight). The generic style of an infographic.
Project Deadline Extended
Reason: Not enough submissions received.
No optimal design (i.e. creative and attractive) received.

Brief has been updated with samples.

Target Market(s)
Very high profile people (e.g. presidents, ministers, GM,...etc.)
Industry/Entity Type
Hotel
Colors
Look and feel

```html
<!DOCTYPE html>
<html lang="en">
<head>
<meta charset="utf-8">
<title>Event Agenda – Welcome</title>
<link href="https://fonts.googleapis.com/css2?family=Roboto+Slab:wght@400;700&family=Open+Sans:wght@400;600&display=swap" rel="stylesheet">
<style>
  :root {
    --paper: #e8e9ea;
    --grey-top: #7f8082;
    --grey-mid: #8c8d8f;
    --panel-dark: #58585a;
    --red: #c92f2b;
    --red-deep: #861628;
    --white: #f2f2f2;
    --ink: #111111;
    --oval: #e4e4e4;
    --slab: "Roboto Slab", "Rockwell", serif;
    --sans: "Open Sans", Arial, sans-serif;
  }
  html, body { margin: 0; padding: 0; overflow: hidden; }
  body { width: 1200px; height: 1200px; background: var(--paper); }
  .agenda { position: relative; width: 1200px; height: 1200px; overflow: hidden; background: var(--paper); font-family: var(--slab); }
  .backdrop { position: absolute; inset: 0; }
  .abs { position: absolute; margin: 0; }
  .title-welcome { left: 0; width: 548px; top: 226px; text-align: right; font-size: 72px; font-weight: 700; color: var(--white); letter-spacing: 1px; line-height: 1; }
  .title-event { left: 0; width: 443px; top: 425px; text-align: center; font-size: 70px; font-weight: 700; color: var(--white); line-height: 1.02; letter-spacing: 1px; }
  .logo-slot { left: 458px; top: 409px; width: 236px; height: 122px; border-radius: 50%; background: var(--oval); display: flex; align-items: center; justify-content: center; font-family: var(--sans); font-size: 33px; font-weight: 600; color: #3a3a3a; letter-spacing: -0.5px; }
  .tagline { left: 455px; width: 250px; top: 559px; text-align: center; font-size: 17px; line-height: 22px; color: var(--white); }
  .date-label { left: 397px; top: 638px; font-family: var(--sans); font-size: 28px; font-weight: 600; color: var(--white); }
  .date-value { left: 397px; top: 672px; font-family: var(--sans); font-size: 40px; color: var(--white); letter-spacing: 1px; }
  .person { color: var(--white); font-size: 30px; font-weight: 700; line-height: 35px; text-align: center; width: 200px; letter-spacing: 0.5px; }
  .field { left: 25px; font-size: 20px; font-weight: 700; color: var(--ink); }
  .schedule { left: 25px; top: 946px; list-style: none; padding: 0; font-size: 20px; font-weight: 700; color: var(--ink); }
  .schedule li { height: 36.4px; white-space: nowrap; }
  .roles-head { left: 560px; top: 982px; width: 226px; text-align: right; font-size: 20px; font-weight: 700; line-height: 36.4px; color: var(--ink); }
  .roles { left: 821px; top: 982px; list-style: none; padding: 0; font-size: 20px; font-weight: 700; color: var(--ink); }
  .roles li { height: 36.4px; white-space: nowrap; }
</style>
</head>
<body>
<main class="agenda">
  <svg class="backdrop" width="1200" height="1200" viewBox="0 0 1200 1200" aria-hidden="true">
    <defs>
      <linearGradient id="redFade" x1="0" y1="0" x2="1" y2="0">
        <stop offset="0" stop-color="#c92f2b"/>
        <stop offset="0.55" stop-color="#c42d2c"/>
        <stop offset="1" stop-color="#861628"/>
      </linearGradient>
      <linearGradient id="greyFade" x1="0" y1="0" x2="0" y2="1">
        <stop offset="0" stop-color="#808183"/>
        <stop offset="1" stop-color="#8e8f91"/>
      </linearGradient>
      <linearGradient id="curlSheen" x1="0" y1="0" x2="1" y2="1">
        <stop offset="0" stop-color="#9a9a9a"/>
        <stop offset="0.45" stop-color="#ffffff"/>
        <stop offset="1" stop-color="#cfcfcf"/>
      </linearGradient>
      <radialGradient id="portraitFill" cx="0.5" cy="0.75" r="0.7">
        <stop offset="0" stop-color="#d8d8d8"/>
        <stop offset="1" stop-color="#555557"/>
      </radialGradient>
    </defs>
    <!-- red band -->
    <rect x="372" y="0" width="828" height="958" fill="url(#redFade)"/>
    <!-- grey cover -->
    <path d="M0 0 H720 V645 L620 735 H372 V615 H0 Z" fill="url(#greyFade)"/>
    <!-- light paper lower-left with peeled corner -->
    <path d="M0 615 H372 V780 L600 958 H1200 V1200 H0 Z" fill="var(--paper)"/>
    <!-- title panels -->
    <rect x="0" y="114" width="575" height="235" fill="var(--panel-dark)"/>
    <rect x="0" y="395" width="443" height="220" fill="var(--panel-dark)"/>
    <!-- small page curl at date -->
    <path d="M720 645 C700 660 690 700 675 690 C665 700 640 725 620 735 Z" fill="url(#curlSheen)"/>
    <!-- large page curl -->
    <path d="M372 780 C395 770 430 760 476 755 C500 820 560 905 600 958 Z" fill="url(#curlSheen)"/>
  </svg>

  <h1 class="abs title-welcome">WELCOME</h1>
  <h2 class="abs title-event">EVENT<br>NAME</h2>
  <div class="abs logo-slot">logo,flag,etc.</div>
  <p class="abs tagline">"Some sentences about the event issues OR add some proverbs."</p>
  <p class="abs date-label">date:</p>
  <p class="abs date-value">31.12.2014</p>

  <svg class="abs" style="left:767px;top:44px" width="206" height="206" role="img" aria-label="Portrait photo of host"><circle cx="103" cy="103" r="103" fill="url(#portraitFill)"/></svg>
  <svg class="abs" style="left:962px;top:264px" width="206" height="206" role="img" aria-label="Portrait photo of host"><circle cx="103" cy="103" r="103" fill="url(#portraitFill)"/></svg>
  <svg class="abs" style="left:767px;top:506px" width="206" height="206" role="img" aria-label="Portrait photo of host"><circle cx="103" cy="103" r="103" fill="url(#portraitFill)"/></svg>
  <svg class="abs" style="left:962px;top:732px" width="206" height="206" role="img" aria-label="Portrait photo of host"><circle cx="103" cy="103" r="103" fill="url(#portraitFill)"/></svg>

  <p class="abs person" style="left:977px;top:119px">Alex Alexia<br>Manager</p>
  <p class="abs person" style="left:743px;top:339px">Alex Alexia<br>Manager</p>
  <p class="abs person" style="left:977px;top:581px">Alex Alexia<br>Manager</p>
  <p class="abs person" style="left:743px;top:806px">Alex Alexia<br>Manager</p>

  <p class="abs field" style="top:692px">Location:</p>
  <p class="abs field" style="top:735px">OBJECTIVE</p>
  <p class="abs field" style="top:822px">SCHEDULE</p>

  <ul class="abs schedule">
    <li>7:30 to 7:45: Welcome – Alex Alexia</li>
    <li>7:45 to 8:15: ............................................. – Alex Alexia</li>
    <li>8:15 to 8:25: ............................................. – Alex Alexia</li>
    <li>8:25 to 9:00: ............................................. – Alex Alexia</li>
    <li>9:00 to 9:15: ............................................. – Alex Alexia</li>
    <li>9:15 to 9:30: ............................................. – Alex Alexia</li>
  </ul>

  <p class="abs roles-head">ROLES/<br>RESPONSIBILITIES</p>
  <ul class="abs roles">
    <li>Set-up: ...................................</li>
    <li>Minutes: ................................</li>
    <li>Paperwork: .........................</li>
    <li>Refreshments: .....................</li>
    <li>Snacks: ................................</li>
  </ul>
</main>
</body>
</html>
```